Kestrel Mobile Wellness Co

I am a Physical Therapist. I want to go to peoples homes and give them quality one on one care for their back/thoracic/neck pain. I will give them spinal mobilizations, massage and exercise. I will do all of this in the comfort of their homes. I will bring my massage table with me so I can work on their back and neck. Fee for service. Accept check and credit cards. I am an orthopaedic specialist and a Spine specialist. I will come to your door so you don't have to come to me.

working class and upper class

Massage

• Something to let the people know they will be treated special. They will get better care with me than if they were in an outpatient setting.

```html
<!DOCTYPE html>
<html lang="en">
<head>
<meta charset="utf-8">
<title>Physical Therapist – Business Card</title>
<link href="https://fonts.googleapis.com/css2?family=Josefin+Sans:ital,wght@0,200;0,300;0,400;1,300&display=swap" rel="stylesheet">
<style>
  :root {
    --stage: #2b2b2b;
    --ink: #111111;
    --paper: #ffffff;
    --blue: #1aa6e4;
    --blue-deep: #0b5fb6;
    --blue-mid: #2a86d6;
    --night: #050505;
    --body-tone: #8a6a55;
  }
  * { margin: 0; padding: 0; box-sizing: border-box; }
  html, body {
    width: 855px; height: 1200px; overflow: hidden;
    background: var(--stage);
    font-family: "Josefin Sans", sans-serif;
  }
  .card {
    position: absolute; left: 86px; width: 682px; height: 516px;
    background: var(--paper); overflow: hidden;
  }
  .card--front { top: 40px; }
  .card--back { top: 582px; }

  /* front */
  .front-dark {
    position: absolute; inset: 0 0 auto 0; height: 360px;
    background: linear-gradient(90deg, var(--night) 0%, #141414 45%, #1f1f1f 100%);
  }
  .hero-photo {
    position: absolute; left: 330px; top: 0; width: 352px; height: 360px;
    background: radial-gradient(ellipse at 55% 45%, #cfcfcf 0%, #8d8d8d 28%, #3a3a3a 55%, #0d0d0d 80%);
  }
  .hero-photo::after {
    content: ""; position: absolute; left: 110px; top: 20px; width: 130px; height: 320px;
    border-radius: 60px 60px 30px 30px;
    background: linear-gradient(180deg, #c9a98a, var(--body-tone));
    opacity: .85;
  }
  .front-wave { position: absolute; left: 0; top: 0; width: 682px; height: 516px; }
  .front-title {
    position: absolute; left: 46px; top: 84px;
    color: var(--paper); font-weight: 200; font-size: 60px; line-height: 64px;
    letter-spacing: -1.5px; text-transform: uppercase;
  }
  .phone-pill {
    position: absolute; display: flex; align-items: stretch;
    border: 3px solid var(--blue); border-radius: 12px; overflow: hidden; background: var(--paper);
  }
  .phone-pill__icon {
    background: var(--blue); display: flex; align-items: center; justify-content: center;
  }
  .phone-pill__number {
    color: var(--blue); font-style: italic; font-weight: 300;
    display: flex; align-items: center; justify-content: center; flex: 1;
  }
  .front-phone { left: 178px; top: 383px; width: 311px; height: 56px; }
  .front-phone .phone-pill__icon { width: 66px; }
  .front-phone .phone-pill__number { font-size: 38px; padding-top: 6px; }
  .tagline {
    position: absolute; left: 0; right: 0; top: 455px; text-align: center;
    font-style: italic; font-weight: 300; font-size: 24px; color: var(--ink);
  }

  /* back */
  .owner-name {
    position: absolute; left: 41px; top: 36px;
    font-size: 29px; font-weight: 400; color: var(--ink); letter-spacing: .5px;
    white-space: nowrap;
  }
  .owner-role {
    position: absolute; left: 42px; top: 69px;
    font-size: 7.5px; font-weight: 400; color: var(--ink); text-transform: uppercase;
    white-space: nowrap;
  }
  .back-phone { left: 264px; top: 35px; width: 223px; height: 42px; border-width: 2px; }
  .back-phone .phone-pill__icon { width: 44px; }
  .back-phone .phone-pill__number { font-size: 27px; padding-top: 4px; }
  .services-panel { position: absolute; left: 0; top: 96px; width: 324px; height: 420px; }
  .service-list {
    position: absolute; left: 30px; top: 186px; list-style: none;
    color: var(--paper); font-size: 21px; font-weight: 300; line-height: 28px;
  }
  .service-list li { position: relative; padding-left: 22px; margin-bottom: 6px; }
  .service-list li::before {
    content: ""; position: absolute; left: 0; top: 7px; width: 12px; height: 12px;
    border-radius: 50%; background: var(--paper);
  }
  .payment-note {
    position: absolute; left: 54px; top: 442px; color: var(--paper); font-size: 12px; font-weight: 300;
  }
  .home-visits {
    position: absolute; left: 41px; top: 465px; width: 213px; height: 28px;
    border: 1.5px solid var(--paper); border-radius: 14px;
    color: var(--paper); font-size: 17px; font-weight: 300; letter-spacing: 2px;
    display: flex; align-items: center; justify-content: center; padding-top: 3px;
  }
</style>
</head>
<body>

<section class="card card--front">
  <div class="front-dark"></div>
  <div class="hero-photo" role="img" aria-label="Photo of a woman's bare back with hands behind her head and the spine highlighted"></div>
  <svg class="front-wave" viewBox="0 0 682 516" aria-hidden="true">
    <defs>
      <linearGradient id="waveBlue" x1="0" x2="1">
        <stop offset="0" stop-color="#1aa6e4"/>
        <stop offset="1" stop-color="#5cc6f2"/>
      </linearGradient>
    </defs>
    <path d="M0 228 C90 270 200 330 330 340 C460 350 560 322 682 326 L682 516 L0 516 Z" fill="url(#waveBlue)"/>
    <path d="M0 236 C90 280 200 342 330 350 C460 356 560 334 682 340 L682 516 L0 516 Z" fill="#ffffff"/>
  </svg>
  <h1 class="front-title">Physical<br>Therapist</h1>
  <div class="phone-pill front-phone">
    <span class="phone-pill__icon">
      <svg width="32" height="32" viewBox="0 0 24 24" aria-hidden="true"><path fill="#fff" d="M6.6 10.8a15.1 15.1 0 0 0 6.6 6.6l2.2-2.2a1 1 0 0 1 1-.25 11.4 11.4 0 0 0 3.6.57 1 1 0 0 1 1 1V20a1 1 0 0 1-1 1A17 17 0 0 1 3 4a1 1 0 0 1 1-1h3.5a1 1 0 0 1 1 1c0 1.25.2 2.45.57 3.57a1 1 0 0 1-.25 1z"/></svg>
    </span>
    <span class="phone-pill__number">555.014.2290</span>
  </div>
  <p class="tagline">I will come to your door so you don’t have to come to me</p>
</section>

<section class="card card--back">
  <svg class="services-panel" viewBox="0 0 324 420" role="img" aria-label="Blue panel with an X-ray style illustration of a human spine and ribcage">
    <defs>
      <linearGradient id="panelBlue" x1="0" y1="0" x2="1" y2="1">
        <stop offset="0" stop-color="#0b5fb6"/>
        <stop offset=".55" stop-color="#2a86d6"/>
        <stop offset="1" stop-color="#7fc2f0"/>
      </linearGradient>
    </defs>
    <path d="M0 14 C90 12 180 0 250 0 Q324 0 324 60 L324 420 L0 420 Z" fill="url(#panelBlue)"/>
  </svg>
  <h2 class="owner-name">DANIEL HART</h2>
  <p class="owner-role">Orthopaedic specialist and spine specialist</p>
  <div class="phone-pill back-phone">
    <span class="phone-pill__icon">
      <svg width="22" height="22" viewBox="0 0 24 24" aria-hidden="true"><path fill="#fff" d="M6.6 10.8a15.1 15.1 0 0 0 6.6 6.6l2.2-2.2a1 1 0 0 1 1-.25 11.4 11.4 0 0 0 3.6.57 1 1 0 0 1 1 1V20a1 1 0 0 1-1 1A17 17 0 0 1 3 4a1 1 0 0 1 1-1h3.5a1 1 0 0 1 1 1c0 1.25.2 2.45.57 3.57a1 1 0 0 1-.25 1z"/></svg>
    </span>
    <span class="phone-pill__number">555.014.2290</span>
  </div>
  <ul class="service-list">
    <li>Spinal mobilization<br>for back pain</li>
    <li>Neck pain</li>
    <li>Thoracic pain</li>
    <li>Body massage</li>
    <li>Physical therapy exercises</li>
  </ul>
  <p class="payment-note">Cheks and credit cards acceptable</p>
  <div class="home-visits">HOME VISITS</div>
</section>

</body>
</html>
```